Business Cards for accounting firm

Need a file and design that we can update for our employees when we get a design we like. Logo is attached.
Megan Tolliver CPA
Owner
P.O. Box 418
Westbrook VT 05831
5553628405
megan@brightlanefin.com
www.brightlanefin.com
Accounting

```html
<!DOCTYPE html>
<html lang="en">
<head>
<meta charset="utf-8">
<title>Brightlane Financial — Business Cards</title>
<link rel="stylesheet" href="https://fonts.googleapis.com/css2?family=Open+Sans:wght@400;600;700&display=swap">
<style>
  :root {
    --bg: #e9e7e3;
    --card-white: #ffffff;
    --card-grey: #77787a;
    --cyan: #2fc0e6;
    --ink: #6b6b6b;
    --ink-soft: #8a8a8a;
    --rule: #9a9a9a;
  }
  * { box-sizing: border-box; margin: 0; padding: 0; }
  html, body { width: 1200px; height: 885px; overflow: hidden; }
  body {
    background: var(--bg);
    font-family: "Open Sans", Arial, sans-serif;
    position: relative;
  }
  .card {
    position: absolute;
    width: 520px;
    height: 297px;
    border-radius: 16px;
    box-shadow: 0 8px 22px rgba(0,0,0,0.18);
    overflow: hidden;
  }
  .card--front { left: 50px; top: 160px; background: var(--card-white); }
  .card--back  { left: 630px; top: 428px; background: var(--card-grey); }

  .brand {
    position: absolute;
    display: flex;
    align-items: center;
    gap: 10px;
  }
  .brand__mark {
    width: 18px; height: 18px; border-radius: 50%;
    background: var(--cyan);
    flex: none;
  }
  .brand__name {
    font-weight: 700;
    color: var(--cyan);
    line-height: 1.05;
  }
  .card--front .brand { left: 34px; top: 46px; }
  .card--front .brand__name { font-size: 30px; width: 190px; }
  .card--back .brand { left: 50%; top: 50%; transform: translate(-50%, -50%); }
  .card--back .brand__mark { width: 24px; height: 24px; }
  .card--back .brand__name { font-size: 40px; color: #ffffff; }

  .person {
    position: absolute;
    right: 34px; top: 48px;
    text-align: right;
  }
  .person__name { color: var(--cyan); font-weight: 700; font-size: 21px; }
  .person__role { color: var(--ink-soft); font-size: 16px; margin-top: 2px; }

  .divider {
    position: absolute;
    left: 34px; right: 34px; top: 148px;
    height: 1px; background: var(--rule);
  }

  .contact {
    position: absolute;
    left: 34px; top: 172px;
    list-style: none;
  }
  .contact__item {
    display: flex; align-items: center; gap: 10px;
    color: var(--ink); font-size: 15px;
    height: 28px;
  }
  .contact__icon {
    width: 20px; height: 20px; border-radius: 3px;
    background: var(--cyan);
    display: flex; align-items: center; justify-content: center;
  }

  .address {
    position: absolute;
    right: 34px; top: 186px;
    text-align: right;
    color: var(--ink); font-size: 15px; line-height: 1.6;
    font-style: normal;
  }
</style>
</head>
<body>
  <section class="card card--front" aria-label="Business card front">
    <div class="brand">
      <span class="brand__mark"></span>
      <span class="brand__name">Brightlane Financial</span>
    </div>
    <div class="person">
      <p class="person__name">Megan Tolliver CPA</p>
      <p class="person__role">Owner</p>
    </div>
    <div class="divider"></div>
    <ul class="contact">
      <li class="contact__item">
        <span class="contact__icon">
          <svg width="12" height="12" viewBox="0 0 24 24"><path fill="#fff" d="M6.6 10.8a15 15 0 0 0 6.6 6.6l2.2-2.2a1 1 0 0 1 1-.25 11.4 11.4 0 0 0 3.6.57 1 1 0 0 1 1 1V20a1 1 0 0 1-1 1A17 17 0 0 1 3 4a1 1 0 0 1 1-1h3.5a1 1 0 0 1 1 1c0 1.25.2 2.45.57 3.57a1 1 0 0 1-.25 1z"/></svg>
        </span>5553628405
      </li>
      <li class="contact__item">
        <span class="contact__icon">
          <svg width="12" height="12" viewBox="0 0 24 24"><rect x="2" y="5" width="20" height="14" fill="none" stroke="#fff" stroke-width="2"/><path d="M2 5l10 8 10-8" fill="none" stroke="#fff" stroke-width="2"/></svg>
        </span>megan@brightlanefin.com
      </li>
      <li class="contact__item">
        <span class="contact__icon">
          <svg width="12" height="12" viewBox="0 0 24 24" fill="none" stroke="#fff" stroke-width="2"><circle cx="12" cy="12" r="9"/><ellipse cx="12" cy="12" rx="4" ry="9"/><path d="M3 12h18"/></svg>
        </span>www.brightlanefin.com
      </li>
    </ul>
    <address class="address">
      P.O. Box 418<br>
      Westbrook VT 05831
    </address>
  </section>

  <section class="card card--back" aria-label="Business card back">
    <div class="brand">
      <span class="brand__mark"></span>
      <span class="brand__name">Brightlane Financial</span>
    </div>
  </section>
</body>
</html>
```